inspirational business card

I want to use the Vector on Pixavend.com (number 58172046) and I will purchase the vector to send it to the designer once the general concept is approved. You can download it for free for a one time use on providing a design for this request.
Within the vector, insert:
Tessa Brundle
Guidance and Partnering

I prefer a vertical card but do not require vertical.

Contact info:

Tessa Brundle, J.D.
Collaborative Lawyer
Certified Divorce Coach
Mediation Coach
PHONE 515/555-0143
EMAIL: tbjd@quellmail.net

Website: Guidanceandpartnering.com
Settlementcourse.com

I like greens, blue and grey. I do not want black font, and would like the font to be legible without needing perfect reading vision (no super small font).
I would like the overall theme to convey growth and nurturance.
I like the vector I selected because of the growth and light portrayed.
Not too frilly or too bold. I would like to to appeal to both sexes.

Target Market(s)

Generally professional women 35-60

Industry/Entity Type

Attorney

Font styles to use
Serif
Sans Serif

Colors
acd136
cadf82
fbf289
9d9d9d

Requirements
Must have
• My project does not need to have my photo but you could use it if you want
Nice to have
• Vertical
• I like rounded edges on the cards
Should not have
• I do not like my name appearing two times in close proximity. I'm not a flowery person.

```html
<!DOCTYPE html>
<html lang="en">
<head>
<meta charset="utf-8">
<title>Tessa Brundle – Business Card</title>
<link href="https://fonts.googleapis.com/css2?family=Arvo:wght@400&family=Montserrat:wght@500;600&display=swap" rel="stylesheet">
<style>
  :root {
    --backdrop: #cfcfcf;
    --paper: #f8f8f3;
    --sky: #27c0ee;
    --sky-deep: #0fa9df;
    --leaf-dark: #1c8a3f;
    --leaf-light: #9fcc3b;
    --ink-blue: #1f63b0;
    --ink-green: #4b9a2e;
    --link-blue: #1b9ad6;
  }
  * { box-sizing: border-box; margin: 0; padding: 0; }
  html, body { width: 1200px; height: 800px; overflow: hidden; }
  body {
    background: var(--backdrop);
    font-family: "Montserrat", Arial, sans-serif;
    position: relative;
  }
  .card {
    position: absolute;
    top: 245px;
    width: 540px;
    height: 309px;
    background: var(--paper);
    border-radius: 10px;
    overflow: hidden;
    box-shadow: 0 6px 18px rgba(0,0,0,0.18);
  }
  .card--front { left: 40px; }
  .card--back { left: 620px; }
  .card__waves {
    position: absolute;
    inset: 0;
    width: 100%;
    height: 100%;
  }
  .brand {
    position: absolute;
    display: flex;
    align-items: center;
    gap: 10px;
  }
  .brand__dot {
    flex: none;
    border-radius: 50%;
    background: var(--sky);
  }
  .brand__name {
    font-weight: 600;
    color: var(--ink-blue);
    text-transform: uppercase;
    letter-spacing: 0.08em;
    line-height: 1.3;
  }
  .card--front .brand { top: 38px; right: 28px; width: 170px; }
  .card--front .brand__dot { width: 22px; height: 22px; }
  .card--front .brand__name { font-size: 11px; }
  .card--back .brand { top: 92px; left: 250px; width: 220px; }
  .card--back .brand__dot { width: 30px; height: 30px; }
  .card--back .brand__name { font-size: 15px; }

  .identity {
    position: absolute;
    top: 104px;
    left: 40px;
  }
  .identity__name {
    font-family: "Arvo", Georgia, serif;
    font-weight: 400;
    font-size: 25px;
    color: var(--ink-blue);
    letter-spacing: 0.01em;
  }
  .identity__role {
    font-size: 10.5px;
    font-weight: 600;
    color: var(--ink-green);
    text-transform: uppercase;
    letter-spacing: 0.09em;
    line-height: 1.35;
    margin-top: 2px;
  }
  .contact {
    position: absolute;
    top: 180px;
    left: 44px;
    list-style: none;
  }
  .contact__item {
    display: flex;
    align-items: center;
    gap: 8px;
    font-size: 13px;
    font-weight: 500;
    color: var(--link-blue);
    margin-bottom: 7px;
  }
  .contact__icon { width: 12px; height: 12px; flex: none; }
</style>
</head>
<body>

<section class="card card--front" aria-label="Business card front">
  <svg class="card__waves" viewBox="0 0 540 309" preserveAspectRatio="none" aria-hidden="true">
    <defs>
      <linearGradient id="leafFront" x1="0" y1="0" x2="1" y2="0">
        <stop offset="0" stop-color="#1c8a3f"/>
        <stop offset="0.45" stop-color="#9fcc3b"/>
        <stop offset="1" stop-color="#1c8a3f"/>
      </linearGradient>
    </defs>
    <path d="M0,285 C200,268 400,180 540,95 L540,128 C400,205 200,283 0,300 Z" fill="url(#leafFront)"/>
    <path d="M0,300 C200,283 400,205 540,128 L540,309 L0,309 Z" fill="#27c0ee"/>
  </svg>

  <div class="brand">
    <span class="brand__dot"></span>
    <span class="brand__name">Guidance and Partnering</span>
  </div>

  <div class="identity">
    <h1 class="identity__name">Tessa Brundle, J.D.</h1>
    <p class="identity__role">Collaborative Lawyer</p>
    <p class="identity__role">Certified Divorce Coach</p>
  </div>

  <ul class="contact">
    <li class="contact__item">
      <svg class="contact__icon" viewBox="0 0 12 12" aria-hidden="true"><path d="M2.5,0.8 L4.3,0.8 L5,3.3 L3.8,4.3 C4.5,5.8 6.2,7.5 7.7,8.2 L8.7,7 L11.2,7.7 L11.2,9.5 C11.2,10.5 10.4,11.2 9.5,11.2 C5,11 1,7 0.8,2.5 C0.8,1.6 1.5,0.8 2.5,0.8 Z" fill="#1c8a3f"/></svg>
      <span>515/555-0143</span>
    </li>
    <li class="contact__item">
      <svg class="contact__icon" viewBox="0 0 12 12" aria-hidden="true"><rect x="0.5" y="2" width="11" height="8" fill="#1c8a3f"/><path d="M0.5,2 L6,6.5 L11.5,2" fill="none" stroke="#f8f8f3" stroke-width="1"/></svg>
      <span>tbjd@quellmail.net</span>
    </li>
    <li class="contact__item">
      <svg class="contact__icon" viewBox="0 0 12 12" aria-hidden="true"><circle cx="6" cy="6" r="5.5" fill="#1c8a3f"/><path d="M6,0.5 C3.5,3 3.5,9 6,11.5 M6,0.5 C8.5,3 8.5,9 6,11.5 M0.5,6 L11.5,6" fill="none" stroke="#f8f8f3" stroke-width="0.8"/></svg>
      <span>Guidanceandpartnering.com</span>
    </li>
  </ul>
</section>

<section class="card card--back" aria-label="Business card back">
  <svg class="card__waves" viewBox="0 0 540 309" preserveAspectRatio="none" aria-hidden="true">
    <defs>
      <linearGradient id="leafBack" x1="0" y1="0" x2="1" y2="1">
        <stop offset="0" stop-color="#1c8a3f"/>
        <stop offset="0.5" stop-color="#9fcc3b"/>
        <stop offset="1" stop-color="#1c8a3f"/>
      </linearGradient>
    </defs>
    <path d="M0,0 L215,0 C140,60 60,150 0,235 Z" fill="#27c0ee"/>
    <path d="M215,0 L262,0 C170,70 80,165 0,272 L0,235 C60,150 140,60 215,0 Z" fill="url(#leafBack)"/>
    <path d="M262,0 L275,0 C180,72 90,168 0,280 L0,272 C80,165 170,70 262,0 Z" fill="#0fa9df"/>
    <path d="M250,309 C370,255 460,160 540,30 L540,62 C470,175 385,262 292,309 Z" fill="url(#leafBack)"/>
    <path d="M292,309 C385,262 470,175 540,62 L540,309 Z" fill="#27c0ee"/>
  </svg>

  <div class="brand">
    <span class="brand__dot"></span>
    <span class="brand__name">Guidance and Partnering</span>
  </div>
</section>

</body>
</html>
```